Travlo Investor Pitch Deck - Text For Slides Provided

Design Brief for Travlo Pitch Deck

1. Brand Consistency:
• Use Travlo’s colors (primary and accent colors) and branding elements throughout the deck. Stick to clean, modern typography that aligns with Travlo’s brand identity.
2. Visual Storytelling:
• Design the slides to tell a clear narrative, with each slide building on the next. Use a mix of bold headlines, concise subheadings, and key bullet points. Limit text where possible, using strong visuals to reinforce the messaging.
3. Infographics & Data Visuals:
• For the financial model and valuation slides, create engaging, easy-to-understand charts and infographics. Focus on bar graphs, pie charts, and line graphs to clearly show projected growth and market opportunities.
4. Impactful Imagery:
• Incorporate relevant moving industry imagery (e.g., trucks, boxes, AI/digital themes) to emphasize the innovation and operational focus of Travlo. Include subtle animations to guide the viewer through the story.
5. Executive Summary & Key Slides:
• Make the executive summary slide punchy with high-level icons or graphics to quickly communicate Travlo’s value proposition. On the problem/solution slides, visually depict the inefficiencies of middlemen with a contrast to Travlo’s streamlined, tech-driven solution.
6. Focus on Key Metrics:
• Highlight important metrics, such as valuation targets, growth projections, and financial milestones, with large, bold numbers and simple charts. Keep these data points at the forefront of key slides.
7. Story-Driven Layout:
• Structure the deck so that it flows smoothly—each slide should feel like a natural progression of the narrative, leading to a clear conclusion of why Travlo is the future of the moving industry.

Target Market(s)

Private Equity Investors

Industry/Entity Type

Professional Moving

Font styles to use
Sans Serif
Other font styles liked:
• see fonts in the attached presentations

Colors
0054AA
0677BA
7BADD7
CADEEF
E8F1F8
FFC000
F8CF3A
FAE287
FDF2CF
FEFAEE

Requirements
Must have
• Noted in the project description but I have attached the text for every slide
Nice to have
• I need you to use the outlines for every slide in the word document and what I want is to take the text and make them more graphical and tell a story. I have included some of our other presentations as attachments so you can understand the look and feel

```html
<!DOCTYPE html>
<html lang="en">
<head>
<meta charset="utf-8">
<title>Travlo Investor Pitch Deck</title>
<link href="https://fonts.googleapis.com/css2?family=Poppins:wght@400;500;600;700&display=swap" rel="stylesheet">
<style>
:root{
  --blue:#0054AA;
  --blue-2:#0677BA;
  --blue-3:#7BADD7;
  --blue-4:#CADEEF;
  --blue-5:#E8F1F8;
  --gold:#FFC000;
  --gold-2:#F8CF3A;
  --gold-3:#FAE287;
  --gold-4:#FDF2CF;
  --ink:#1d2533;
  --muted:#5b6270;
  --page:#ffffff;
}
*{box-sizing:border-box;margin:0;padding:0}
html,body{width:1200px;height:2194px;overflow:hidden;background:var(--page)}
body{position:relative;font-family:'Poppins',sans-serif;color:var(--ink)}

.slide{position:absolute;width:637px;height:357px;background:#fff;overflow:hidden;
  transform:scale(.8517);transform-origin:0 0;box-shadow:0 5px 16px rgba(20,40,80,.16)}
.col-l{left:37.5px}.col-r{left:620px}
.row-1{top:171px}.row-2{top:558px}.row-3{top:944.6px}.row-4{top:1331px}.row-5{top:1718px}

.abs{position:absolute}
.footer{position:absolute;left:0;right:0;top:332px;height:19px;background:var(--gold-2);z-index:2;
  display:flex;align-items:center;justify-content:space-between;padding:0 20px 0 22px;font-size:6px;color:var(--blue-2)}
.footer .brand{display:flex;align-items:center;gap:4px;font-size:9px;font-weight:600;color:var(--blue)}
.footer .brand i{width:7px;height:7px;background:var(--blue);display:block}
.footer .copy{position:absolute;left:0;right:0;text-align:center;pointer-events:none}

.kicker{font-size:8.5px;font-weight:600;color:var(--ink)}
.title{font-size:22px;font-weight:600;color:var(--blue);line-height:1.25}
.title small{font-size:11px;font-weight:400;color:var(--ink)}
.title .mark{border-bottom:2px solid var(--gold)}
.title-c{position:absolute;left:0;right:0;text-align:center}
.sub{font-size:8.5px;color:var(--ink);text-align:center}

.card{position:absolute;background:#fff;border:1px solid var(--gold-3);border-radius:10px;
  box-shadow:0 3px 9px rgba(0,84,170,.12);padding:8px 9px}
.card h3{font-size:9px;font-weight:600;color:var(--blue);line-height:1.2;margin-bottom:5px}
.card p,.card li{font-size:6px;line-height:1.4;color:var(--muted)}
.card ul{padding-left:8px}
.card li{margin-bottom:5px}
.card.center{text-align:center}
.icon{width:17px;height:17px;display:block;margin-bottom:6px}
.card .stat{font-size:21px;font-weight:700;color:var(--ink);text-align:center;line-height:1.1}
.card .cap{font-size:5px;color:var(--muted);text-align:center;line-height:1.3}
.card .tag{font-size:8px;font-weight:600;color:var(--blue);text-align:center;line-height:1.25}
.card .big{font-size:22px;font-weight:600;color:var(--blue);line-height:1.1;margin-bottom:8px}

.photo{position:absolute;border-radius:24px;background:#eef1f6;padding:10px;box-shadow:0 4px 12px rgba(0,0,0,.08)}
.photo .fill{width:100%;height:100%;border-radius:18px}

/* financial table */
.fin{position:absolute;display:flex;flex-direction:column;font-size:4.2px;color:var(--ink);
  border-left:1px solid var(--blue-4);border-right:1px solid var(--blue-4);background:#fff}
.fin .r{flex:1;display:flex;align-items:center;padding:0 4px;border-bottom:1px solid #eef0f4}
.fin .r span:first-child{width:58px;flex:none;font-weight:500}
.fin .n{flex:1;text-align:justify;text-align-last:justify}
.fin .h{background:var(--gold-2);color:var(--blue);font-weight:600}
.fin .b{background:var(--blue-2);color:#fff;font-weight:600}
.fin .gap{flex:0 0 4px;border:none}
</style>
</head>
<body>

<!-- 1 Executive summary -->
<section class="slide col-l row-1">
  <h1 class="title title-c" style="top:22px"><span class="mark">Executive Summary</span></h1>
  <p class="sub abs" style="left:0;right:0;top:55px">Travlo: Revolutionizing the Moving Industry with AI</p>

  <div class="card center" style="left:68px;top:83px;width:180px;height:229px;padding:56px 12px 0">
    <h3 style="font-size:13px;margin-bottom:10px">Overview:</h3>
    <p>Travlo is transforming the $90-100B moving industry by leveraging AI, GPS, and automated compliance to deliver the first instant guaranteed pricing platform.<br>We’re cutting out inefficiencies and middlemen to improve costs and service quality.</p>
  </div>
  <div class="card" style="left:261px;top:83px;width:148px;height:114px">
    <h3 style="text-align:center">Proven Model:</h3>
    <ul><li>Successfully raised $1.9M to build a $5M appraised tech stack.</li>
    <li>Raised an additional $500K to prove the B2I model successfully.</li></ul>
  </div>
  <div class="card" style="left:422px;top:83px;width:147px;height:114px">
    <h3 style="text-align:center">Market Strategy:</h3>
    <p>Focus on B2I (local movers) first to reach $10M EBITDA within 24 months, leading to a $150M valuation.</p>
    <p style="margin-top:5px">Expand into B2B and B2C markets with a $50M Series B for full-scale growth.</p>
  </div>
  <div class="card" style="left:261px;top:203px;width:148px;height:111px">
    <h3 style="text-align:center">Valuation Targets:</h3>
    <ul><li>B2I (10% of local movers): $600M valuation.</li>
    <li>B2B (2.5% of Apex 1000): $100M valuation.</li>
    <li>B2C (1% B2C market): $1.8B valuation.</li></ul>
  </div>
  <div class="card center" style="left:422px;top:203px;width:147px;height:111px">
    <h3>Why Now:</h3>
    <p>Travlo is uniquely positioned to disrupt the market with AI-powered pricing, automated compliance, and proven scalability in B2I—poised to expand into B2B and B2C.</p>
  </div>
  <footer class="footer"><span class="brand"><i></i>Travlo</span><span class="copy">© Copyrights Travlo</span><span>— 1</span></footer>
</section>

<!-- 2 Problem -->
<section class="slide col-r row-1">
  <p class="kicker abs" style="left:41px;top:27px">The Problem –</p>
  <h1 class="title abs" style="left:41px;top:40px">Inefficiencies in the<br>Moving Industry</h1>
  <div class="card" style="left:42px;top:133px;width:107px;height:163px">
    <svg class="icon" viewBox="0 0 20 20"><circle cx="9" cy="9" r="6" fill="none" stroke="#0054AA" stroke-width="1.5"/><path d="M5 9h2l1-2 2 4 1-2h2M13.5 13.5 18 18" fill="none" stroke="#0054AA" stroke-width="1.5"/></svg>
    <h3>Market<br>Overview:</h3>
    <p>The moving industry is plagued by middlemen—van lines, brokers, and agents—who drive up costs by 15-40% without adding value. These layers result in inflated prices and poor service quality for consumers.</p>
  </div>
  <div class="card" style="left:167px;top:133px;width:106px;height:163px">
    <svg class="icon" viewBox="0 0 20 20"><circle cx="10" cy="10" r="7" fill="none" stroke="#0054AA" stroke-width="1.5"/><path d="M10 5v10M7 8h5a2 2 0 0 1 0 4H8" fill="none" stroke="#0054AA" stroke-width="1.3"/></svg>
    <h3>Triple<br>Margining:</h3>
    <p>Van lines, agents, and brokers each take a cut, leaving frontline movers underpaid and service quality compromised.</p>
  </div>
  <div class="card" style="left:291px;top:133px;width:108px;height:163px">
    <svg class="icon" viewBox="0 0 20 20"><rect x="4" y="2" width="12" height="16" rx="1.5" fill="none" stroke="#0054AA" stroke-width="1.5"/><path d="M7 6h6M7 10h6M7 14h4" stroke="#0054AA" stroke-width="1.3"/></svg>
    <h3>Lack of<br>Accountability:</h3>
    <p>Service failures, missed deadlines, and damaged goods are common due to poor communication between middlemen. The customer is left with no clear party to hold accountable.</p>
  </div>
  <div class="photo" style="left:412px;top:27px;width:205px;height:297px">
    <div class="fill" role="img" aria-label="Photo of two movers packing cardboard boxes in an office" style="background:linear-gradient(160deg,#b9c7d6 0%,#8d9db0 40%,#a4825e 75%,#c9a57c 100%)"></div>
  </div>
  <footer class="footer"><span class="brand"><i></i>Travlo</span><span class="copy">© Copyrights Travlo</span><span>— 2</span></footer>
</section>

<!-- 3 Solution -->
<section class="slide col-l row-2">
  <div class="photo" style="left:8px;top:25px;width:206px;height:295px">
    <div class="fill" role="img" aria-label="Photo of a hand holding a phone surrounded by glowing logistics icons" style="background:linear-gradient(150deg,#4d6a86 0%,#25405c 50%,#5c7b99 100%)"></div>
  </div>
  <p class="kicker abs" style="left:242px;top:27px">The Solution -</p>
  <h1 class="title abs" style="left:242px;top:40px">Travlo’s AI-<br>Powered Platform</h1>
  <div class="abs" style="left:242px;top:104px;width:36px;height:2px;background:var(--gold)"></div>
  <div class="card" style="left:166px;top:133px;width:106px;height:162px">
    <svg class="icon" viewBox="0 0 20 20"><circle cx="9" cy="9" r="6" fill="none" stroke="#0054AA" stroke-width="1.5"/><path d="M13.5 13.5 18 18M6 9h6" stroke="#0054AA" stroke-width="1.5"/></svg>
    <h3>Cutting Out<br>Middlemen:</h3>
    <p>Travlo directly connects customers with local movers, eliminating van lines, brokers, and agents. This streamlines the process and ensures transparent, fair pricing.</p>
  </div>
  <div class="card" style="left:278px;top:133px;width:106px;height:162px">
    <svg class="icon" viewBox="0 0 20 20"><circle cx="10" cy="10" r="7" fill="none" stroke="#0054AA" stroke-width="1.5"/><path d="M10 5v10M7 8h5a2 2 0 0 1 0 4H8" fill="none" stroke="#0054AA" stroke-width="1.3"/></svg>
    <h3>AI-Driven<br>Instant Pricing:</h3>
    <p>Travlo offers the industry’s only instant, guaranteed pricing using AI, GPS, and key moving variables.</p>
  </div>
  <div class="card" style="left:392px;top:133px;width:106px;height:162px">
    <svg class="icon" viewBox="0 0 20 20"><rect x="4" y="2" width="12" height="16" rx="1.5" fill="none" stroke="#0054AA" stroke-width="1.5"/><path d="M7 6h6M7 10h6M7 14h4" stroke="#0054AA" stroke-width="1.3"/></svg>
    <h3>Automated<br>Compliance:</h3>
    <p>Fully automates interstate regulatory compliance, reducing legal risks for all movers in the supply chain.</p>
  </div>
  <div class="card" style="left:505px;top:133px;width:107px;height:162px">
    <svg class="icon" viewBox="0 0 20 20"><rect x="4" y="2" width="12" height="16" rx="1.5" fill="none" stroke="#0054AA" stroke-width="1.5"/><path d="M7 7h6M7 11h6" stroke="#0054AA" stroke-width="1.3"/></svg>
    <h3>Real-Time<br>Capacity<br>Matching:</h3>
    <p>The platform optimizes truck capacity by matching real-time availability with customer move requests, improving operational efficiency.</p>
  </div>
  <footer class="footer"><span class="brand"><i></i>Travlo</span><span class="copy">© Copyrights Travlo</span><span>— 3</span></footer>
</section>

<!-- 4 Opportunity B2I -->
<section class="slide col-r row-2">
  <h1 class="title title-c" style="top:22px">The Opportunity – <span class="mark">Targeting B2I</span> <small>(Local Movers)</small></h1>
  <div class="card center" style="left:20px;top:83px;width:130px;height:117px">
    <h3>Why B2I First?:</h3>
    <p>B2I (local movers) represents the most immediate and scalable opportunity for Travlo. The software’s AI-driven pricing and capacity optimization allow local movers to keep their trucks busy and maximize revenue.</p>
  </div>
  <div class="card center" style="left:20px;top:203px;width:130px;height:109px">
    <h3 style="margin-top:6px">Proven B2I Model:</h3>
    <p>We’ve successfully proven the B2I model, adding one new B2I customer per week, each averaging four moves/month or 72 moves/year. This provides consistent, recurring revenue for Travlo.</p>
  </div>
  <div class="card" style="left:155px;top:83px;width:145px;height:33px;padding:4px"><p class="tag">Expected Financial<br>Results</p></div>
  <div class="card" style="left:155px;top:122px;width:145px;height:59px;padding:5px"><p class="tag" style="font-size:7px">Annual Moves from B2I:</p><p class="stat">XXX</p><p class="cap">moves/year from new B2I customers.</p></div>
  <div class="card" style="left:155px;top:186px;width:145px;height:59px;padding:5px"><p class="tag" style="font-size:7px">Gross Profit:</p><p class="stat">$XXX</p><p class="cap">(Estimated)</p></div>
  <div class="card" style="left:155px;top:251px;width:145px;height:61px;padding:5px"><p class="tag" style="font-size:7px">EBITDA:</p><p class="stat">$XXX</p><p class="cap">(Projected over the next 24 months.)</p></div>
  <div class="fin" style="left:312px;top:83px;width:305px;height:229px">
    <div class="r h"><span>REVENUE</span><span class="n">JAN FEB MAR APR MAY JUN JUL AUG SEP OCT NOV DEC 2023</span></div>
    <div class="r"><span>Accounting services</span><span class="n">20,660 21,135 22,885 22,705 23,510 22,825 23,590 23,885 24,110 25,800 26,810 27,980 287,715</span></div>
    <div class="r"><span>Financial Advisory</span><span class="n">1,650 2,650 2,750 4,250 5,500 4,250 5,500 4,250 5,500 6,250 7,000 7,000 58,750</span></div>
    <div class="r"><span>Setup fees</span><span class="n">1,050 1,125 1,175 1,183 1,183 788 788 788 1,183 1,175 1,175 1,175 13,335</span></div>
    <div class="r"><span>Other services</span><span class="n">200 200 200 200 200 200 200 200 200 200 200 200 2,400</span></div>
    <div class="r gap"></div>
    <div class="r h"><span>COST OF REVENUE</span><span class="n"></span></div>
    <div class="r"><span>Accounting</span><span class="n">8,900 8,650 9,750 10,650 11,025 11,225 11,225 11,225 11,225 11,225 11,225 11,225 127,650</span></div>
    <div class="r"><span>HR Salaries</span><span class="n">2,925 2,925 2,925 2,975 3,375 3,375 3,375 3,375 3,375 3,375 3,375 3,650 40,425</span></div>
    <div class="r"><span>Cost of Revenue</span><span class="n">125 125 125 125 125 125 125 125 125 125 125 125 1,500</span></div>
    <div class="r"><span>Gateway Fees</span><span class="n">32 36 40 44 48 52 58 64 71 78 86 94 706</span></div>
    <div class="r b"><span>GROSS PROFIT 60%</span><span class="n">14,448 16,449 19,422 19,836 21,333 19,844 19,844 19,843 22,497 25,282 27,384 28,731 264,336</span></div>
    <div class="r gap"></div>
    <div class="r h"><span>OPERATING COST</span><span class="n"></span></div>
    <div class="r"><span>Rent</span><span class="n">1,550 1,550 1,550 1,550 1,550 1,550 1,550 1,550 1,550 1,550 1,550 1,550 18,600</span></div>
    <div class="r"><span>Audit fees</span><span class="n">85 85 85 85 85 85 85 85 85 85 85 85 1,020</span></div>
    <div class="r"><span>Marketing Expenses</span><span class="n">1,300 1,300 1,300 1,300 1,300 1,300 1,300 1,300 1,300 1,300 1,300 1,300 15,600</span></div>
    <div class="r b"><span>TOTAL OPERATING COST</span><span class="n">8,001 7,963 8,080 8,305 8,530 8,516 8,516 8,516 8,711 8,416 8,418 8,500 103,335</span></div>
    <div class="r gap"></div>
    <div class="r b"><span>NET INCOME 43%</span><span class="n">6,480 10,505 11,442 11,427 12,795 10,295 11,295 11,205 13,672 14,305 16,818 18,231 152,906</span></div>
  </div>
  <footer class="footer"><span class="brand"><i></i>Travlo</span><span class="copy">© Copyrights Travlo</span><span>— 4</span></footer>
</section>

<!-- 5 B2B -->
<section class="slide col-l row-3">
  <h1 class="title title-c" style="top:22px"><span class="mark">Expanding into B2B</span> <small>(Corporate Relocation)</small></h1>
  <div class="card" style="left:20px;top:74px;width:102px;height:229px">
    <svg class="icon" viewBox="0 0 20 20"><path d="M2 10l4-4 4 3 4-3 4 4-6 5z" fill="none" stroke="#0054AA" stroke-width="1.5" stroke-linejoin="round"/></svg>
    <h3>Corporate<br>Relocation<br>Partnerships:</h3>
    <p>After proving the B2I model, Travlo will expand into B2B, focusing on corporate relocation services for Apex 1000 companies. This segment provides high-margin opportunities and long-term contracts.</p>
  </div>
  <div class="card" style="left:137px;top:74px;width:145px;height:33px;padding:4px"><p class="tag">Expected Financial<br>Results</p></div>
  <div class="card" style="left:137px;top:113px;width:145px;height:59px;padding:5px"><p class="tag" style="font-size:7px">Annual Moves from B2I:</p><p class="stat">XXX</p><p class="cap">moves/year from new B2I customers.</p></div>
  <div class="card" style="left:137px;top:178px;width:145px;height:59px;padding:5px"><p class="tag" style="font-size:7px">Gross Profit:</p><p class="stat">$XXX</p><p class="cap">(Estimated)</p></div>
  <div class="card" style="left:137px;top:243px;width:145px;height:60px;padding:5px"><p class="tag" style="font-size:7px">EBITDA:</p><p class="stat">$XXX</p><p class="cap">(Projected over the next 24 months.)</p></div>
  <div class="fin" style="left:296px;top:74px;width:320px;height:229px">
    <div class="r h"><span>REVENUE</span><span class="n">JAN FEB MAR APR MAY JUN JUL AUG SEP OCT NOV DEC 2023</span></div>
    <div class="r"><span>Accounting services</span><span class="n">20,660 21,135 22,885 22,705 23,510 22,825 23,590 23,885 24,110 25,800 26,810 27,980 287,715</span></div>
    <div class="r"><span>Financial Advisory</span><span class="n">1,650 2,650 2,750 4,250 5,500 4,250 5,500 4,250 5,500 6,250 7,000 7,000 58,750</span></div>
    <div class="r"><span>Setup fees</span><span class="n">1,050 1,125 1,175 1,183 1,183 788 788 788 1,183 1,175 1,175 1,175 13,335</span></div>
    <div class="r"><span>Other services</span><span class="n">200 200 200 200 200 200 200 200 200 200 200 200 2,400</span></div>
    <div class="r gap"></div>
    <div class="r h"><span>COST OF REVENUE</span><span class="n"></span></div>
    <div class="r"><span>Accounting</span><span class="n">8,900 8,650 9,750 10,650 11,025 11,225 11,225 11,225 11,225 11,225 11,225 11,225 127,650</span></div>
    <div class="r"><span>HR Salaries</span><span class="n">2,925 2,925 2,925 2,975 3,375 3,375 3,375 3,375 3,375 3,375 3,375 3,650 40,425</span></div>
    <div class="r"><span>Cost of Revenue</span><span class="n">125 125 125 125 125 125 125 125 125 125 125 125 1,500</span></div>
    <div class="r"><span>Gateway Fees</span><span class="n">32 36 40 44 48 52 58 64 71 78 86 94 706</span></div>
    <div class="r b"><span>GROSS PROFIT 60%</span><span class="n">14,448 16,449 19,422 19,836 21,333 19,844 19,844 19,843 22,497 25,282 27,384 28,731 264,336</span></div>
    <div class="r gap"></div>
    <div class="r h"><span>OPERATING COST</span><span class="n"></span></div>
    <div class="r"><span>Rent</span><span class="n">1,550 1,550 1,550 1,550 1,550 1,550 1,550 1,550 1,550 1,550 1,550 1,550 18,600</span></div>
    <div class="r"><span>Audit fees</span><span class="n">85 85 85 85 85 85 85 85 85 85 85 85 1,020</span></div>
    <div class="r"><span>Marketing Expenses</span><span class="n">1,300 1,300 1,300 1,300 1,300 1,300 1,300 1,300 1,300 1,300 1,300 1,300 15,600</span></div>
    <div class="r b"><span>TOTAL OPERATING COST</span><span class="n">8,001 7,963 8,080 8,305 8,530 8,516 8,516 8,516 8,711 8,416 8,418 8,500 103,335</span></div>
    <div class="r gap"></div>
    <div class="r b"><span>NET INCOME 43%</span><span class="n">6,480 10,505 11,442 11,427 12,795 10,295 11,295 11,205 13,672 14,305 16,818 18,231 152,906</span></div>
  </div>
  <footer class="footer"><span class="brand"><i></i>Travlo</span><span class="copy">© Copyrights Travlo</span><span>— 5</span></footer>
</section>

<!-- 6 B2C -->
<section class="slide col-r row-3">
  <h1 class="title title-c" style="top:22px"><span class="mark">Attacking B2C</span> <small>(Consumer Moving Market)</small></h1>
  <div class="card" style="left:22px;top:74px;width:101px;height:229px">
    <svg class="icon" viewBox="0 0 20 20"><circle cx="7" cy="5" r="2.5" fill="#0054AA"/><circle cx="14" cy="5" r="2.5" fill="#0054AA"/><path d="M3 18v-7a3 3 0 0 1 6 0v7M11 18v-7a3 3 0 0 1 6 0v7" fill="#0054AA"/></svg>
    <h3>B2C Strategy:</h3>
    <p>With the foundation of B2I and B2B, Travlo will enter the B2C market with a large-scale acquisition strategy requiring significant branding and credibility investment, similar to Shiftly.</p>
  </div>
  <div class="card" style="left:135px;top:74px;width:147px;height:30px;padding:3px"><p class="tag">Expected Financial<br>Results</p></div>
  <div class="card" style="left:135px;top:108px;width:147px;height:42px;padding:3px"><p class="tag" style="font-size:7px">Customer Acquisition Cost:</p><p class="stat" style="font-size:17px">XXX</p><p class="cap" style="font-size:4.5px">Estimated high 4-figures to low 5-figures.</p></div>
  <div class="card" style="left:135px;top:155px;width:147px;height:42px;padding:3px"><p class="tag" style="font-size:7px">Annual Moves from B2I:</p><p class="stat" style="font-size:17px">XXX</p><p class="cap" style="font-size:4.5px">moves/year from new B2I customers.</p></div>
  <div class="card" style="left:135px;top:201px;width:147px;height:42px;padding:3px"><p class="tag" style="font-size:7px">Gross Profit:</p><p class="stat" style="font-size:17px">$XXX</p><p class="cap" style="font-size:4.5px">(Estimated)</p></div>
  <div class="card" style="left:135px;top:247px;width:147px;height:56px;padding:4px"><p class="tag" style="font-size:7px">EBITDA:</p><p class="stat" style="font-size:18px">$XXX</p><p class="cap" style="font-size:4.5px">(Projected over the next 24 months.)</p></div>
  <div class="fin" style="left:297px;top:74px;width:320px;height:229px">
    <div class="r h"><span>REVENUE</span><span class="n">JAN FEB MAR APR MAY JUN JUL AUG SEP OCT NOV DEC 2023</span></div>
    <div class="r"><span>Accounting services</span><span class="n">20,660 21,135 22,885 22,705 23,510 22,825 23,590 23,885 24,110 25,800 26,810 27,980 287,715</span></div>
    <div class="r"><span>Financial Advisory</span><span class="n">1,650 2,650 2,750 4,250 5,500 4,250 5,500 4,250 5,500 6,250 7,000 7,000 58,750</span></div>
    <div class="r"><span>Setup fees</span><span class="n">1,050 1,125 1,175 1,183 1,183 788 788 788 1,183 1,175 1,175 1,175 13,335</span></div>
    <div class="r"><span>Other services</span><span class="n">200 200 200 200 200 200 200 200 200 200 200 200 2,400</span></div>
    <div class="r gap"></div>
    <div class="r h"><span>COST OF REVENUE</span><span class="n"></span></div>
    <div class="r"><span>Accounting</span><span class="n">8,900 8,650 9,750 10,650 11,025 11,225 11,225 11,225 11,225 11,225 11,225 11,225 127,650</span></div>
    <div class="r"><span>HR Salaries</span><span class="n">2,925 2,925 2,925 2,975 3,375 3,375 3,375 3,375 3,375 3,375 3,375 3,650 40,425</span></div>
    <div class="r"><span>Cost of Revenue</span><span class="n">125 125 125 125 125 125 125 125 125 125 125 125 1,500</span></div>
    <div class="r"><span>Gateway Fees</span><span class="n">32 36 40 44 48 52 58 64 71 78 86 94 706</span></div>
    <div class="r b"><span>GROSS PROFIT 60%</span><span class="n">14,448 16,449 19,422 19,836 21,333 19,844 19,844 19,843 22,497 25,282 27,384 28,731 264,336</span></div>
    <div class="r gap"></div>
    <div class="r h"><span>OPERATING COST</span><span class="n"></span></div>
    <div class="r"><span>Rent</span><span class="n">1,550 1,550 1,550 1,550 1,550 1,550 1,550 1,550 1,550 1,550 1,550 1,550 18,600</span></div>
    <div class="r"><span>Audit fees</span><span class="n">85 85 85 85 85 85 85 85 85 85 85 85 1,020</span></div>
    <div class="r"><span>Marketing Expenses</span><span class="n">1,300 1,300 1,300 1,300 1,300 1,300 1,300 1,300 1,300 1,300 1,300 1,300 15,600</span></div>
    <div class="r b"><span>TOTAL OPERATING COST</span><span class="n">8,001 7,963 8,080 8,305 8,530 8,516 8,516 8,516 8,711 8,416 8,418 8,500 103,335</span></div>
    <div class="r gap"></div>
    <div class="r b"><span>NET INCOME 43%</span><span class="n">6,480 10,505 11,442 11,427 12,795 10,295 11,295 11,205 13,672 14,305 16,818 18,231 152,906</span></div>
  </div>
  <footer class="footer"><span class="brand"><i></i>Travlo</span><span class="copy">© Copyrights Travlo</span><span>— 6</span></footer>
</section>

<!-- 7 Valuation growth -->
<section class="slide col-l row-4">
  <h1 class="title abs" style="left:22px;top:22px;font-size:18px"><span class="mark">Financial Projections and Valuation Growth</span> <span style="color:var(--ink)">– B2I, B2B, B2C</span></h1>
  <div class="card" style="left:20px;top:82px;width:232px;height:57px;padding:9px 10px 0 42px">
    <svg class="abs" style="left:12px;top:14px;width:20px;height:20px" viewBox="0 0 20 20"><path d="M4 10a6 6 0 0 1 10-4.5M16 10a6 6 0 0 1-10 4.5" fill="none" stroke="#0054AA" stroke-width="1.6"/><path d="M14 2v4h-4M6 18v-4h4" fill="none" stroke="#0054AA" stroke-width="1.6"/></svg>
    <h3 style="font-size:10px;margin-bottom:3px">B2I Valuation Growth:</h3><p style="font-size:7px">Targeting 10% of local movers, leading to a $600M valuation.</p>
  </div>
  <div class="card" style="left:20px;top:159px;width:232px;height:58px;padding:9px 10px 0 42px">
    <svg class="abs" style="left:12px;top:14px;width:20px;height:20px" viewBox="0 0 20 20"><path d="M4 10a6 6 0 0 1 10-4.5M16 10a6 6 0 0 1-10 4.5" fill="none" stroke="#0054AA" stroke-width="1.6"/><path d="M14 2v4h-4M6 18v-4h4" fill="none" stroke="#0054AA" stroke-width="1.6"/></svg>
    <h3 style="font-size:10px;margin-bottom:3px">B2B Valuation Growth:</h3><p style="font-size:7px">Targeting 2.5% of Apex 1000, resulting in a $100M valuation.</p>
  </div>
  <div class="card" style="left:20px;top:239px;width:232px;height:58px;padding:9px 10px 0 42px">
    <svg class="abs" style="left:12px;top:14px;width:20px;height:20px" viewBox="0 0 20 20"><path d="M4 10a6 6 0 0 1 10-4.5M16 10a6 6 0 0 1-10 4.5" fill="none" stroke="#0054AA" stroke-width="1.6"/><path d="M14 2v4h-4M6 18v-4h4" fill="none" stroke="#0054AA" stroke-width="1.6"/></svg>
    <h3 style="font-size:10px;margin-bottom:3px">B2C Valuation Growth:</h3><p style="font-size:7px">With 1% of the B2C market, Travlo’s valuation will reach $1.8B.</p>
  </div>
  <div class="fin" style="left:296px;top:73px;width:320px;height:231px">
    <div class="r h"><span>REVENUE</span><span class="n">JAN FEB MAR APR MAY JUN JUL AUG SEP OCT NOV DEC 2023</span></div>
    <div class="r"><span>Accounting services</span><span class="n">20,660 21,135 22,885 22,705 23,510 22,825 23,590 23,885 24,110 25,800 26,810 27,980 287,715</span></div>
    <div class="r"><span>Financial Advisory</span><span class="n">1,650 2,650 2,750 4,250 5,500 4,250 5,500 4,250 5,500 6,250 7,000 7,000 58,750</span></div>
    <div class="r"><span>Setup fees</span><span class="n">1,050 1,125 1,175 1,183 1,183 788 788 788 1,183 1,175 1,175 1,175 13,335</span></div>
    <div class="r"><span>Other services</span><span class="n">200 200 200 200 200 200 200 200 200 200 200 200 2,400</span></div>
    <div class="r gap"></div>
    <div class="r h"><span>COST OF REVENUE</span><span class="n"></span></div>
    <div class="r"><span>Accounting</span><span class="n">8,900 8,650 9,750 10,650 11,025 11,225 11,225 11,225 11,225 11,225 11,225 11,225 127,650</span></div>
    <div class="r"><span>HR Salaries</span><span class="n">2,925 2,925 2,925 2,975 3,375 3,375 3,375 3,375 3,375 3,375 3,375 3,650 40,425</span></div>
    <div class="r"><span>Cost of Revenue</span><span class="n">125 125 125 125 125 125 125 125 125 125 125 125 1,500</span></div>
    <div class="r"><span>Gateway Fees</span><span class="n">32 36 40 44 48 52 58 64 71 78 86 94 706</span></div>
    <div class="r b"><span>GROSS PROFIT 60%</span><span class="n">14,448 16,449 19,422 19,836 21,333 19,844 19,844 19,843 22,497 25,282 27,384 28,731 264,336</span></div>
    <div class="r gap"></div>
    <div class="r h"><span>OPERATING COST</span><span class="n"></span></div>
    <div class="r"><span>Rent</span><span class="n">1,550 1,550 1,550 1,550 1,550 1,550 1,550 1,550 1,550 1,550 1,550 1,550 18,600</span></div>
    <div class="r"><span>Audit fees</span><span class="n">85 85 85 85 85 85 85 85 85 85 85 85 1,020</span></div>
    <div class="r"><span>Marketing Expenses</span><span class="n">1,300 1,300 1,300 1,300 1,300 1,300 1,300 1,300 1,300 1,300 1,300 1,300 15,600</span></div>
    <div class="r b"><span>TOTAL OPERATING COST</span><span class="n">8,001 7,963 8,080 8,305 8,530 8,516 8,516 8,516 8,711 8,416 8,418 8,500 103,335</span></div>
    <div class="r gap"></div>
    <div class="r b"><span>NET INCOME 43%</span><span class="n">6,480 10,505 11,442 11,427 12,795 10,295 11,295 11,205 13,672 14,305 16,818 18,231 152,906</span></div>
  </div>
  <footer class="footer"><span class="brand"><i></i>Travlo</span><span class="copy">© Copyrights Travlo</span><span>— 7</span></footer>
</section>

<!-- 8 Traction -->
<section class="slide col-r row-4">
  <h1 class="title title-c" style="top:20px"><span class="mark">Traction</span></h1>
  <p class="sub abs" style="left:0;right:0;top:54px">What We’ve Achieved So Far</p>
  <div class="card" style="left:32px;top:98px;width:106px;height:164px;padding:12px 10px">
    <p class="big">$5M</p><h3>Tech Stack Built and Appraised at $5M:</h3><p>Travlo’s tech stack is already appraised at $5M, proving our innovation is ready for market.</p>
  </div>
  <div class="card" style="left:146px;top:98px;width:106px;height:164px;padding:12px 10px">
    <p class="big">$1.9M</p><h3>Seed<br>Raised:</h3><p>Used to build the platform and conduct early market tests.</p>
  </div>
  <div class="card" style="left:260px;top:98px;width:108px;height:164px;padding:12px 10px">
    <p class="big">$500k</p><h3>Supplemental<br>Raised:</h3><p>Successfully raised to prove the B2I model, demonstrating scalable revenue generation.</p>
  </div>
  <div class="card" style="left:375px;top:98px;width:107px;height:164px;padding:12px 10px">
    <p class="big">B2I</p><h3>Proven B2I<br>Model:</h3><p>Consistent customer acquisition with one new B2I customer per week.</p>
  </div>
  <div class="card" style="left:489px;top:98px;width:108px;height:164px;padding:12px 10px">
    <p class="big">TEAM</p><h3>Team<br>Restructuring:</h3><p>Brought in a Best-in-Class management team of industry veterans to lead Travlo into its next growth phase.</p>
  </div>
  <footer class="footer"><span class="brand"><i></i>Travlo</span><span class="copy">© Copyrights Travlo</span><span>— 8</span></footer>
</section>

<!-- 9 Use of funds -->
<section class="slide col-l row-5">
  <h1 class="title title-c" style="top:22px"><span class="mark">Use of Funds</span> <span style="color:var(--ink);font-weight:400">– Round A</span></h1>
  <svg class="abs" style="left:0;top:0" width="637" height="357" viewBox="0 0 637 357">
    <g fill="none" stroke="#0054AA" stroke-width="1">
      <path d="M164 185H193"/><path d="M189 182l4 3-4 3"/>
      <path d="M297 185L334 115M297 185H334M297 185L334 255"/>
      <path d="M330 113l4 2-2 4M330 182l4 3-4 3M332 251l2 4-4 2"/>
    </g>
  </svg>
  <div class="card" style="left:45px;top:126px;width:119px;height:119px;padding:10px 12px">
    <svg class="icon" viewBox="0 0 20 20"><circle cx="9" cy="9" r="6" fill="none" stroke="#0054AA" stroke-width="1.5"/><path d="M13.5 13.5 18 18M6 9h6M9 6v6" stroke="#0054AA" stroke-width="1.5"/></svg>
    <h3>Round A Focus:</h3>
    <p>Invest heavily into B2I (primarily) and B2B (secondarily) to reach $10M EBITDA within 24 months.</p>
  </div>
  <div class="card" style="left:196px;top:136px;width:101px;height:99px;display:flex;align-items:center;justify-content:center">
    <h3 style="text-align:center;margin:0">Use of<br>Proceeds:</h3>
  </div>
  <div class="card" style="left:345px;top:87px;width:230px;height:57px;padding:10px 10px 0 42px">
    <svg class="abs" style="left:14px;top:14px;width:18px;height:18px" viewBox="0 0 20 20"><rect x="2" y="2" width="7" height="7" fill="none" stroke="#0054AA" stroke-width="1.5"/><rect x="11" y="2" width="7" height="7" fill="none" stroke="#0054AA" stroke-width="1.5"/><rect x="2" y="11" width="7" height="7" fill="none" stroke="#0054AA" stroke-width="1.5"/><path d="M11 11h3v3h4v4h-7z" fill="#0054AA"/></svg>
    <h3 style="font-size:10px;margin-bottom:2px">Technology Development</h3><p style="font-size:7px">Enhance AI capabilities for pricing and capacity matching.</p>
  </div>
  <div class="card" style="left:345px;top:156px;width:230px;height:58px;padding:10px 10px 0 42px">
    <svg class="abs" style="left:14px;top:14px;width:18px;height:18px" viewBox="0 0 20 20"><rect x="2" y="10" width="16" height="8" fill="#0054AA"/><rect x="6" y="3" width="8" height="6" fill="none" stroke="#0054AA" stroke-width="1.5"/></svg>
    <h3 style="font-size:10px;margin-bottom:2px">Sales &amp; Marketing:</h3><p style="font-size:7px">Accelerate customer acquisition for B2I and B2B.</p>
  </div>
  <div class="card" style="left:345px;top:226px;width:230px;height:58px;padding:10px 10px 0 42px">
    <svg class="abs" style="left:14px;top:14px;width:18px;height:18px" viewBox="0 0 20 20"><circle cx="10" cy="6" r="3" fill="#0054AA"/><path d="M4 18c0-5 3-7 6-7s6 2 6 7z" fill="#0054AA"/></svg>
    <h3 style="font-size:10px;margin-bottom:2px">Team Expansion:</h3><p style="font-size:7px">Recruit key talent to drive operational growth.</p>
  </div>
  <footer class="footer"><span class="brand"><i></i>Travlo</span><span class="copy">© Copyrights Travlo</span><span>— 9</span></footer>
</section>

<!-- 10 Why Travlo -->
<section class="slide col-r row-5">
  <p class="kicker abs" style="left:41px;top:27px">Why Travlo –</p>
  <h1 class="title abs" style="left:41px;top:44px;display:flex;align-items:center;gap:8px"><i style="width:14px;height:14px;background:var(--blue);display:block"></i><span>Travlo <span style="color:var(--blue)">The Future of Moving</span></span></h1>
  <div class="abs" role="img" aria-label="Photo of a futuristic warehouse conveyor carrying a cardboard box" style="left:-10px;top:88px;width:278px;height:278px;border-radius:50%;border:10px solid #eef1f6;background:radial-gradient(circle at 50% 55%,#bfe6f5 0%,#4a8cb8 35%,#1e3f63 75%,#12263d 100%)"></div>
  <div class="card" style="left:325px;top:95px;width:232px;height:81px;padding:10px 10px 0 42px">
    <svg class="abs" style="left:12px;top:14px;width:20px;height:20px" viewBox="0 0 20 20"><circle cx="10" cy="10" r="8" fill="#0054AA"/><path d="M7 13V8a3 3 0 0 1 6 0" fill="none" stroke="#fff" stroke-width="1.5"/></svg>
    <h3 style="font-size:10px;margin-bottom:4px">The Only AI-Driven Instant Pricing Platform:</h3><p>No competitor in the moving industry offers instant, guaranteed pricing powered by AI.</p>
  </div>
  <div class="card" style="left:325px;top:192px;width:232px;height:82px;padding:10px 10px 0 42px">
    <svg class="abs" style="left:12px;top:14px;width:20px;height:20px" viewBox="0 0 20 20"><circle cx="10" cy="10" r="8" fill="none" stroke="#0054AA" stroke-width="1.5"/><circle cx="10" cy="10" r="4" fill="none" stroke="#0054AA" stroke-width="1.5"/><circle cx="10" cy="10" r="1.5" fill="#0054AA"/></svg>
    <h3 style="font-size:10px;margin-bottom:4px">Massive Market<br>Opportunity:</h3><p>With a total addressable market cap of</p><p style="font-size:9px;font-weight:700;color:var(--ink)">**$2.5B+</p>
  </div>
  <footer class="footer"><span class="brand"><i></i>Travlo</span><span class="copy">© Copyrights Travlo</span><span>— 10</span></footer>
</section>

</body>
</html>
```